Business Card

We would like a very clean corporate, two sided business card that conveys that we are a quality focused, reliable organisation that can make a business better. We focus on a cycle of continuous improvement for IT systems.

The brief is primarily clean and corporate, nothing overly complicated.

We sell IT services, IT support, server implementation, problem solving services to businesses in Australia.

Business

```html
<!DOCTYPE html>
<html lang="en">
<head>
<meta charset="utf-8">
<title>Northvale Systems – Business Card Back</title>
<link rel="stylesheet" href="https://fonts.googleapis.com/css2?family=Poppins:wght@600&family=Questrial&display=swap">
<style>
  :root {
    --card-red: #ff0000;
    --ink-white: #ffffff;
  }
  * { margin: 0; padding: 0; box-sizing: border-box; }
  html, body {
    width: 1200px;
    height: 783px;
    overflow: hidden;
    background: var(--card-red);
  }
  .card {
    position: relative;
    width: 1200px;
    height: 783px;
    background: var(--card-red);
    color: var(--ink-white);
    font-family: "Questrial", "Century Gothic", sans-serif;
  }
  .brand-name {
    position: absolute;
    left: 675px;
    top: 225px;
    width: 380px;
    text-align: center;
    font-size: 46px;
    letter-spacing: 1px;
    line-height: 1;
    color: var(--ink-white);
  }
  .address,
  .contact {
    position: absolute;
    left: 120px;
    font-size: 31px;
    line-height: 39px;
    font-style: normal;
  }
  .address { top: 346px; }
  .contact { top: 553px; }
  .contact .label {
    font-family: "Poppins", "Century Gothic", sans-serif;
    font-weight: 600;
    font-size: 29px;
  }
</style>
</head>
<body>
  <main class="card">
    <div class="brand-name">Northvale</div>

    <address class="address">
      Northvale Systems Pty Ltd<br>
      Suite 210, 14-18 Carrow Lane<br>
      Westbrook, NSW, 2071<br>
      Australia
    </address>

    <div class="contact">
      <div><span class="label">PH:</span> +61 2 9100 4821</div>
      <div><span class="label">FAX:</span> +61 2 9100 4839</div>
      <div><span class="label">ABN:</span> 47 183 556 209</div>
    </div>
  </main>
</body>
</html>
```